Financial Services Consultant needs a business card

We need a business card for a new consulting company based in Melbourne called
"Korvane Metrics". Tagline is Assess, Adjust, Grow
We would like to see business card designs that are in line with the minimal style of the website www.korvane-metrics-example.com
The font I have used on the website is Proxima Nova and would like the same or similar font used on the business card with a minimal design in line with the website Two sided with "KORVANE METRICS" ASSESS, ADJUST, GROW on one side and name, title and contact details on the otther
Updates

Hi All, thanks for your submissions, much appreciated.

I have recently added some colour to my webiste, it is hex #3a7b74 for those that wish to use it
Thanks

Hi all

thanks very much for your design submissions I am very impressed and they are much appreciated.

Interms of general feedback please find below;

Colour: I am trying to stick to a minimal design and colour scheme for my website which is still under construction, up to 3 colours( www.korvane-metrics-example.com) it is currently black and white with a small amount of blue/green but I am open to suggestion/interpretations for a consulting company.

Card: I dont mind if it has rounded edges or straight, I was thinking about using a letterpress card if possible

Detail: the detail on the card will include; Name, Title, Mobile, Personal Email, Business Email,Web,Business Address

Once again thanks for submissions

Industry/Entity Type

Business

```html
<!DOCTYPE html>
<html lang="en">
<head>
<meta charset="utf-8">
<title>Korvane Metrics – Business Card</title>
<link rel="stylesheet" href="https://fonts.googleapis.com/css2?family=Montserrat:wght@600;700&family=Open+Sans:wght@400;600&display=swap">
<style>
  :root {
    --page-bg: #e9e9e7;
    --card-white: #ffffff;
    --ink: #141414;
    --band: #1c1b1b;
    --teal: #3a7b74;
    --muted: #3c3c3c;
    --on-dark: #f2f2f2;
    --divider: #9a9a9a;
  }
  * { box-sizing: border-box; margin: 0; padding: 0; }
  html, body {
    width: 1200px; height: 720px; overflow: hidden;
    background: var(--page-bg);
    font-family: "Open Sans", Arial, sans-serif;
  }
  .sheet {
    width: 1200px; height: 720px;
    display: flex; align-items: center; justify-content: center; gap: 40px;
  }
  .card {
    position: relative;
    width: 540px; height: 309px;
    background: var(--card-white);
    box-shadow: 0 6px 18px rgba(0,0,0,0.14);
    overflow: hidden;
  }

  /* Contact side */
  .card--contact .brand-name {
    position: absolute; left: 38px; top: 38px;
    font-family: "Montserrat", Arial, sans-serif;
    font-weight: 700; font-size: 34px; letter-spacing: 4px; line-height: 1.2;
    color: var(--ink); white-space: nowrap;
  }
  .card--contact .person {
    position: absolute; left: 0; right: 0; top: 110px;
    text-align: center;
    font-size: 16px; font-weight: 600; color: var(--muted);
  }
  .card--contact .person .title { color: var(--teal); font-weight: 400; font-size: 14px; }
  .accent-line {
    position: absolute; left: 0; right: 0; top: 152px;
    height: 2px; background: var(--teal);
  }
  .contact-band {
    position: absolute; left: 0; right: 0; top: 157px; bottom: 0;
    background: var(--band); color: var(--on-dark);
    display: flex; align-items: center; justify-content: center; gap: 18px;
    font-size: 14px; line-height: 1.55;
  }
  .address { text-align: right; white-space: nowrap; }
  .band-divider { width: 1px; height: 48px; background: var(--divider); }
  .contact-list { list-style: none; }
  .contact-list li { display: flex; align-items: center; gap: 7px; white-space: nowrap; }
  .contact-list svg { width: 13px; height: 13px; flex: none; }

  /* Brand side */
  .card--brand .lockup {
    position: absolute; left: 0; right: 0; top: 92px;
    text-align: center;
  }
  .card--brand .brand-name {
    font-family: "Montserrat", Arial, sans-serif;
    font-weight: 700; font-size: 38px; letter-spacing: 4px; line-height: 1.2;
    color: var(--ink); white-space: nowrap;
  }
  .card--brand .tagline {
    margin-top: 6px; font-size: 15px; color: var(--muted);
  }
  .card--brand .web {
    position: absolute; left: 0; right: 0; bottom: 44px;
    text-align: center; font-size: 15px; letter-spacing: 3px; color: var(--muted);
    white-space: nowrap;
  }
  .card--brand .web strong { font-weight: 600; color: var(--ink); }
</style>
</head>
<body>
<main class="sheet">

  <section class="card card--contact" aria-label="Card front: contact details">
    <h1 class="brand-name">KORVANE METRICS</h1>
    <p class="person">Your Name, <span class="title">Title</span></p>
    <div class="accent-line"></div>
    <div class="contact-band">
      <p class="address">Street Name, City Name<br>State Zip Code</p>
      <span class="band-divider"></span>
      <ul class="contact-list">
        <li>
          <svg viewBox="0 0 16 16" aria-hidden="true"><circle cx="8" cy="8" r="7" fill="none" stroke="currentColor" stroke-width="1.5"/><path d="M5.5 4.5l1.5 0 .8 2-1 .8a5 5 0 0 0 1.9 1.9l.8-1 2 .8v1.5a1 1 0 0 1-1 1A6 6 0 0 1 4.5 5.5a1 1 0 0 1 1-1z" fill="currentColor"/></svg>
          555-010-2468
        </li>
        <li>
          <svg viewBox="0 0 16 16" aria-hidden="true"><circle cx="8" cy="8" r="7" fill="none" stroke="currentColor" stroke-width="1.5"/><ellipse cx="8" cy="8" rx="3" ry="7" fill="none" stroke="currentColor" stroke-width="1.2"/><path d="M1 8h14" stroke="currentColor" stroke-width="1.2"/></svg>
          www.korvane-metrics-example.com
        </li>
      </ul>
    </div>
  </section>

  <section class="card card--brand" aria-label="Card back: brand and tagline">
    <div class="lockup">
      <h2 class="brand-name">KORVANE METRICS</h2>
      <p class="tagline">Assess, Adjust, Grow</p>
    </div>
    <p class="web">www.<strong>korvane-metrics-example</strong>.com</p>
  </section>

</main>
</body>
</html>
```